Luxury Business Card Design for High-End Window Treatments

Gilded Vantages
Custom Plantation Shutters & Architectural Shading Systems

⸻

BACK

Daniel Forsythe
Owner

Custom Interior & Exterior Window Treatments

919-482-7034
gildedvantages.com

I have included a picture that I’m hoping we can use on the back, but I’m also wondering if you can get rid of the ladder? Should we get rid of shutters , shades and blinds underneath Gilded Vantages?

Target Market(s)

High-end residential homeowners, custom home builders, architects, interior designers, and luxury renovation clients seeking premium plantation shutters and motorized architectural shading systems.

Industry/Entity Type

Custom Window treatments

Contact Information for Business Card

Front Gilded Vantages Custom Plantation Shutters Motorized Architectural Shading Systems BACK Daniel Forsythe Owner 919-482-7034 GildedVantages.com Custom Interior & Exterior Window Treatments By Appointment

Requirements
Nice to have
• Not 100% sure on nice to halves or the color but you can definitely check out my website to get a better understanding of what I’m trying to do

```html
<!DOCTYPE html>
<html lang="en">
<head>
<meta charset="utf-8">
<title>Gilded Vantages – Business Card</title>
<link rel="stylesheet" href="https://fonts.googleapis.com/css2?family=Poppins:wght@400;500&family=Montserrat:wght@400&display=swap">
<style>
  :root {
    --gold: #d4b03a;
    --black: #000000;
    --page: #ffffff;
    --photo-warm: #6e5443;
    --photo-mid: #7d7872;
    --photo-cool: #4a4a46;
    --veil-edge: rgba(20, 18, 16, 0.55);
    --veil-inner: rgba(30, 28, 26, 0.2);
    --band: rgba(40, 38, 36, 0.8);
  }
  * { margin: 0; padding: 0; box-sizing: border-box; }
  html, body { width: 972px; height: 1200px; overflow: hidden; background: var(--page); }
  .canvas { position: relative; width: 972px; height: 1200px; }

  .card { position: absolute; left: 136px; width: 700px; height: 400px; overflow: hidden; }

  /* Front */
  .card-front { top: 168px; background: var(--black); }
  .brand-name {
    position: absolute; left: 0; right: 0; top: 81px;
    text-align: center; color: var(--gold);
    font-family: "Poppins", sans-serif; font-weight: 400;
    font-size: 90px; line-height: 119px; letter-spacing: 0.5px;
  }
  .brand-rule {
    position: absolute; left: 98px; width: 504px; top: 336px;
    height: 1px; background: var(--gold);
  }
  .brand-tagline {
    position: absolute; left: 0; right: 0; top: 344px;
    text-align: center; color: var(--gold);
    font-family: "Montserrat", sans-serif; font-size: 14.6px; letter-spacing: 0.2px;
  }

  /* Back */
  .card-back { top: 634px; }
  .porch-photo {
    position: absolute; inset: 0;
    background: linear-gradient(110deg, var(--photo-warm) 0%, var(--photo-mid) 45%, var(--photo-cool) 100%);
  }
  .photo-veil {
    position: absolute; inset: 0;
    border: 30px solid var(--veil-edge);
    background: var(--veil-inner);
  }
  .contact-frame {
    position: absolute; left: 167px; top: 81px; width: 367px; height: 237px;
    border: 2px solid var(--gold);
    background: rgba(40, 36, 30, 0.3);
  }
  .person-name, .person-role, .contact-phone, .contact-web, .service-line {
    position: absolute; left: 0; right: 0; text-align: center;
    color: var(--gold); font-family: "Poppins", sans-serif; font-weight: 400;
  }
  .person-name { top: 98px; font-size: 40px; font-weight: 500; line-height: 48px; }
  .person-role { top: 143px; font-size: 20px; line-height: 28px; }
  .contact-phone { top: 249px; font-size: 22px; line-height: 28px; }
  .contact-web { top: 276px; font-size: 22px; line-height: 28px; }
  .service-band {
    position: absolute; left: 30px; right: 0; bottom: 0; height: 30px;
    background: var(--band);
  }
  .service-line { bottom: 5px; font-size: 16px; line-height: 20px; }
</style>
</head>
<body>
<div class="canvas">
  <section class="card card-front">
    <h1 class="brand-name">Gilded<br>Vantages</h1>
    <div class="brand-rule"></div>
    <p class="brand-tagline">Custom Plantation Shutters Motorized Architectural Shading Systems</p>
  </section>

  <section class="card card-back">
    <div class="porch-photo" role="img" aria-label="Photo of a home porch with a wooden front door, white brick, louvered shutters, windows and pink flowers"></div>
    <div class="photo-veil"></div>
    <div class="contact-frame"></div>
    <p class="person-name">Daniel Forsythe</p>
    <p class="person-role">OWNER</p>
    <p class="contact-phone">919-482-7034</p>
    <p class="contact-web">GildedVantages.com</p>
    <div class="service-band"></div>
    <p class="service-line">Custom Interior &amp; Exterior Window Treatments By Appointment</p>
  </section>
</div>
</body>
</html>
```